Tervolan Pty Ltd professional business card

A professional business card template using the colours from the supplied logo.
Clean crisp lines while, Modern while not being over the top.

Target Market(s)

Construction, commerical and industrial

Industry/Entity Type

Communications

Contact Information for Business Card

For a Communications, IT, Optical fibre installation company

Colors
37b8a4

```html
<!DOCTYPE html>
<html lang="en">
<head>
<meta charset="utf-8">
<title>Tervolan Pty Ltd — Business Card</title>
<link rel="stylesheet" href="https://fonts.googleapis.com/css2?family=Montserrat:wght@500;700&family=Inter:wght@400&display=swap">
<style>
  :root {
    --page-bg: #e4e4e4;
    --card-bg: #141415;
    --card-bg-light: #1d1d1f;
    --brand-teal: #1b9aa8;
    --curve-teal: #2f5d64;
    --wordmark-grey: #707175;
    --contact-grey: #8b8c90;
    --rule-grey: #6a6b6e;
  }
  * { margin: 0; padding: 0; box-sizing: border-box; }
  html, body {
    width: 1200px;
    height: 1200px;
    overflow: hidden;
    background: var(--page-bg);
  }
  .sheet {
    position: relative;
    width: 1200px;
    height: 1200px;
  }
  .card {
    position: absolute;
    left: 192px;
    width: 836px;
    height: 477px;
    border-radius: 12px;
    overflow: hidden;
    background: radial-gradient(ellipse at 70% 30%, var(--card-bg-light) 0%, var(--card-bg) 65%);
  }
  .card--front { top: 71px; }
  .card--back  { top: 595px; }

  .blueprint-area {
    position: absolute;
    top: 0;
    right: 0;
    width: 230px;
    height: 100%;
    background: linear-gradient(200deg, rgba(255,255,255,0.045) 0%, rgba(255,255,255,0.015) 60%, rgba(255,255,255,0) 100%);
  }
  .blueprint-area--left {
    left: 0;
    right: auto;
    top: auto;
    bottom: 0;
    width: 240px;
    height: 260px;
    background: radial-gradient(circle at 20% 60%, rgba(255,255,255,0.03) 0%, rgba(255,255,255,0) 70%);
  }

  .wordmark {
    position: absolute;
    display: flex;
    align-items: center;
    font-family: "Montserrat", sans-serif;
    font-weight: 500;
    color: var(--wordmark-grey);
    white-space: nowrap;
  }
  .wordmark__dot {
    border-radius: 50%;
    background: var(--brand-teal);
    flex: none;
  }
  .card--front .wordmark {
    left: 50%;
    top: 50%;
    transform: translate(-50%, -50%);
    font-size: 58px;
    gap: 16px;
  }
  .card--front .wordmark__dot { width: 34px; height: 34px; }
  .card--back .wordmark {
    left: 75px;
    top: 56px;
    font-size: 36px;
    gap: 10px;
  }
  .card--back .wordmark__dot { width: 22px; height: 22px; }

  .holder-name {
    position: absolute;
    left: 65px;
    top: 228px;
    font-family: "Montserrat", sans-serif;
    font-weight: 700;
    font-size: 32px;
    letter-spacing: 1.5px;
    color: var(--brand-teal);
    text-transform: uppercase;
  }
  .contact-list {
    position: absolute;
    left: 66px;
    top: 308px;
    list-style: none;
    font-family: "Inter", sans-serif;
    font-weight: 400;
    font-size: 18px;
    line-height: 27px;
    letter-spacing: 0.6px;
    color: var(--contact-grey);
  }
  .card-lines {
    position: absolute;
    inset: 0;
  }
</style>
</head>
<body>
<main class="sheet">

  <section class="card card--front" aria-label="Card front">
    <div class="blueprint-area" role="img" aria-label="Faint architectural blueprint linework"></div>
    <div class="blueprint-area blueprint-area--left" role="img" aria-label="Faint spiral staircase plan linework"></div>
    <div class="wordmark">
      <span class="wordmark__dot"></span>
      <span class="wordmark__name">Tervolan</span>
    </div>
  </section>

  <section class="card card--back" aria-label="Card back">
    <div class="blueprint-area" role="img" aria-label="Faint architectural blueprint linework"></div>
    <div class="blueprint-area blueprint-area--left" role="img" aria-label="Faint spiral staircase plan linework"></div>
    <svg class="card-lines" width="836" height="477" viewBox="0 0 836 477" aria-hidden="true">
      <path d="M370 477 C 600 435 769 260 769 0" fill="none" stroke="var(--curve-teal)" stroke-width="1.6"/>
      <line x1="769" y1="0" x2="769" y2="477" stroke="var(--rule-grey)" stroke-width="1.4"/>
    </svg>
    <div class="wordmark">
      <span class="wordmark__dot"></span>
      <span class="wordmark__name">Tervolan</span>
    </div>
    <h1 class="holder-name">Marlena Okafor</h1>
    <ul class="contact-list">
      <li class="contact-list__phone">077 5550192</li>
      <li class="contact-list__email">admin@tervolan.com</li>
      <li class="contact-list__web">www.tervolan.com</li>
    </ul>
  </section>

</main>
</body>
</html>
```